Valbrook Data Works

Our company is about IT hardwares and IT solutions. IT hardware such as PC, RAMS, storage and servers. IT solutions such as project management, BA. We are also selling new technology too.

Target Market(s)

Consumer, Small to Medium Business, Corporate

Requirements
Must have
• The business card must have the following:
• Name:
• Title:
• Contact Number:
• Email address:
• Website:
• Color: Must match the logo color upgrade

```html
<!DOCTYPE html>
<html lang="en">
<head>
<meta charset="utf-8">
<title>Valbrook Data Works – Business Card</title>
<link href="https://fonts.googleapis.com/css2?family=Lato:wght@400;700;900&display=swap" rel="stylesheet">
<style>
  :root {
    --backdrop: #2b2b2b;
    --paper: #ffffff;
    --charcoal: #474747;
    --ink: #222222;
    --copper: #c4702e;
    --copper-light: #d98a36;
  }
  html, body {
    margin: 0;
    padding: 0;
    width: 1200px;
    height: 1200px;
    overflow: hidden;
    background: var(--backdrop);
    font-family: "Lato", Arial, sans-serif;
  }
  .canvas {
    position: relative;
    width: 1200px;
    height: 1200px;
  }
  .card {
    position: absolute;
    top: 310px;
    height: 594px;
    box-sizing: border-box;
  }
  .card-front {
    left: 234px;
    width: 364px;
    background: var(--paper);
    text-align: center;
  }
  .card-back {
    left: 627px;
    width: 369px;
    background: var(--charcoal);
    overflow: hidden;
  }
  .brand-dot {
    position: absolute;
    left: 50%;
    top: 104px;
    width: 44px;
    height: 44px;
    margin-left: -22px;
    border-radius: 50%;
    background: var(--copper);
  }
  .brand-name {
    position: absolute;
    left: 0;
    right: 0;
    top: 192px;
    margin: 0;
    font-weight: 900;
    font-size: 36px;
    line-height: 42px;
    letter-spacing: 1px;
    color: var(--charcoal);
  }
  .person-name {
    position: absolute;
    left: 0;
    right: 0;
    top: 366px;
    margin: 0;
    font-weight: 700;
    font-size: 21px;
    color: var(--copper);
  }
  .person-title {
    position: absolute;
    left: 0;
    right: 0;
    top: 392px;
    margin: 0;
    font-size: 16px;
    color: var(--ink);
  }
  .contact-divider {
    position: absolute;
    left: 87px;
    top: 446px;
  }
  .contact-list {
    position: absolute;
    left: 0;
    right: 0;
    top: 484px;
    margin: 0;
    padding: 0;
    list-style: none;
    font-size: 16px;
    line-height: 22px;
    color: var(--ink);
  }
  .split-band {
    position: absolute;
    left: 0;
    top: 0;
  }
  .tagline {
    position: absolute;
    left: 0;
    right: 0;
    top: 528px;
    margin: 0;
    text-align: center;
    font-size: 17px;
    color: var(--paper);
  }
</style>
</head>
<body>
<main class="canvas">
  <section class="card card-front">
    <span class="brand-dot"></span>
    <h1 class="brand-name">VALBROOK<br>DATA WORKS</h1>
    <p class="person-name">DANIEL HARROW</p>
    <p class="person-title">Managing Director</p>
    <svg class="contact-divider" width="190" height="26" viewBox="0 0 190 26" aria-hidden="true">
      <line x1="0" y1="13" x2="52" y2="13" stroke="#222" stroke-width="1"/>
      <line x1="138" y1="13" x2="190" y2="13" stroke="#222" stroke-width="1"/>
      <circle cx="68" cy="13" r="12" fill="#c4702e"/>
      <circle cx="95" cy="13" r="12" fill="#c4702e"/>
      <circle cx="122" cy="13" r="12" fill="#c4702e"/>
      <!-- phone -->
      <path d="M62 9 q6 -4 12 0 l-1 2 h-2 l-1 -1 h-4 l-1 1 h-2 z M64 12 h8 l1 5 h-10 z" fill="#fff"/>
      <!-- envelope -->
      <rect x="89" y="9" width="12" height="8" fill="#fff"/>
      <path d="M89 9 l6 5 l6 -5" fill="none" stroke="#c4702e" stroke-width="1"/>
      <!-- globe -->
      <circle cx="122" cy="13" r="6" fill="none" stroke="#fff" stroke-width="1.4"/>
      <ellipse cx="122" cy="13" rx="2.5" ry="6" fill="none" stroke="#fff" stroke-width="1"/>
      <line x1="116" y1="13" x2="128" y2="13" stroke="#fff" stroke-width="1"/>
    </svg>
    <ul class="contact-list">
      <li>044-987 654 321</li>
      <li>info@valbrookdata.com</li>
      <li>www.valbrookdata.com</li>
    </ul>
  </section>

  <section class="card card-back">
    <svg class="split-band" width="369" height="594" viewBox="0 0 369 594" aria-hidden="true">
      <polygon points="0,262 369,372 369,594 0,594" fill="#c4702e"/>
    </svg>
    <p class="tagline">IT HARDWARES AND IT SOLUTIONS</p>
  </section>
</main>
</body>
</html>
```